Marlow Hire Business Card for recruitment company

We are looking for a Business Card Design that incorporates our personal details and our busines name and logo. We are a specialized search consultancy that recruit Property and Construction professionals.
We would like a business card that stands out and is appealing to the Construction and Property industry as well.

Target Market(s)

people in the construction and property industry

Contact Information for Business Card

Business Name and logo

Font styles to use
Serif

Colors
0094D4
00A9DD
6FCCEA
C7EBF8
E9F6FB

Requirements
Must have
• Business name and logo as well as contact details
Should not have
• No photos of us please

```html
<!DOCTYPE html>
<html lang="en">
<head>
<meta charset="utf-8">
<title>Marlow Hire – Business Card</title>
<link rel="stylesheet" href="https://fonts.googleapis.com/css2?family=Lato:wght@400&family=Noto+Serif:wght@400&display=swap">
<style>
  :root {
    --backdrop: #969796;
    --navy: #033a51;
    --paper: #ffffff;
    --band-grey: #9a9b9d;
    --ink-light: #ffffff;
  }
  * { margin: 0; padding: 0; box-sizing: border-box; }
  html, body { width: 1200px; height: 1200px; overflow: hidden; }
  body { background: var(--backdrop); position: relative; font-family: "Lato", sans-serif; }

  .card {
    position: absolute;
    left: 222px;
    width: 755px;
    height: 463px;
    border-radius: 0 30px 0 30px;
    overflow: hidden;
  }
  .card--front { top: 104px; background: var(--navy); }
  .card--back { top: 629px; background: var(--navy); }

  .front-shape { position: absolute; inset: 0; }

  .brand-name {
    position: absolute;
    font-family: "Lato", sans-serif;
    font-weight: 400;
    text-transform: uppercase;
    white-space: nowrap;
  }
  .card--front .brand-name {
    right: 44px;
    top: 52px;
    font-size: 50px;
    letter-spacing: 3px;
    color: var(--navy);
  }

  .person { position: absolute; left: 49px; top: 194px; color: var(--ink-light); font-family: "Noto Serif", serif; }
  .person__name { font-size: 28px; letter-spacing: 1px; line-height: 1.1; }
  .person__role { font-size: 21px; letter-spacing: 0.5px; margin-top: 4px; }

  .contact-list { position: absolute; left: 50px; top: 296px; list-style: none; color: var(--ink-light); }
  .contact-list li { display: flex; align-items: center; height: 33px; font-size: 20px; }
  .contact-list svg { width: 22px; height: 22px; margin-right: 9px; fill: none; stroke: var(--ink-light); stroke-width: 1.8; }

  .address { position: absolute; left: 463px; top: 334px; color: var(--ink-light); font-size: 20px; line-height: 27px; white-space: nowrap; }
  .address svg { display: block; width: 20px; height: 28px; margin-bottom: 6px; fill: var(--ink-light); }

  .back-pattern { position: absolute; inset: 0; background: linear-gradient(160deg, #043d55, #03354a); }
  .card--back .brand-name {
    right: 60px;
    bottom: 90px;
    font-size: 38px;
    letter-spacing: 2px;
    color: var(--ink-light);
  }
</style>
</head>
<body>

<section class="card card--front" aria-label="Business card front">
  <svg class="front-shape" viewBox="0 0 755 463" aria-hidden="true">
    <path d="M10,0 Q330,250 755,270 L755,246 Q330,226 16,0 Z" fill="var(--band-grey)"/>
    <path d="M10,0 Q330,250 755,270" fill="none" stroke="#ffffff" stroke-width="3"/>
    <path d="M16,0 L755,0 L755,246 Q330,226 16,0 Z" fill="var(--paper)"/>
  </svg>

  <div class="brand-name">Marlow Hire</div>

  <div class="person">
    <div class="person__name">Dalton Reeve</div>
    <div class="person__role">President</div>
  </div>

  <ul class="contact-list">
    <li>
      <svg viewBox="0 0 22 22"><rect x="6" y="1.5" width="10" height="19" rx="1.5"/><line x1="6" y1="16" x2="16" y2="16"/></svg>
      014 2785 3316
    </li>
    <li>
      <svg viewBox="0 0 22 22"><path d="M2,8 Q11,1 20,8 L17,10 L15,7 Q11,5.5 7,7 L5,10 Z" fill="#fff"/><rect x="5" y="11" width="12" height="8" rx="2" fill="#fff"/></svg>
      014 2785 3317
    </li>
    <li>
      <svg viewBox="0 0 22 22"><rect x="1.5" y="4" width="16" height="12"/><polyline points="1.5,4 9.5,11 17.5,4"/><circle cx="17" cy="16" r="3.5" fill="#fff"/></svg>
      hello@marlowhire.com
    </li>
    <li>
      <svg viewBox="0 0 22 22"><circle cx="11" cy="11" r="9"/><ellipse cx="11" cy="11" rx="4" ry="9"/><line x1="2" y1="11" x2="20" y2="11"/><line x1="3.5" y1="6.5" x2="18.5" y2="6.5"/><line x1="3.5" y1="15.5" x2="18.5" y2="15.5"/></svg>
      www.marlowhire.com
    </li>
  </ul>

  <div class="address">
    <svg viewBox="0 0 20 28"><path d="M10,0 A9,9 0 0 1 19,9 C19,16 10,27 10,27 C10,27 1,16 1,9 A9,9 0 0 1 10,0 Z M10,5 A4,4 0 1 0 10,13 A4,4 0 1 0 10,5 Z" fill-rule="evenodd"/></svg>
    48 Foundry Lane, Suite 200<br>
    Brookfield, United States 6024
  </div>
</section>

<section class="card card--back" aria-label="Business card back">
  <div class="back-pattern" role="img" aria-label="Repeated tone-on-tone company name pattern across the navy background"></div>
  <div class="brand-name">Marlow Hire</div>
</section>

</body>
</html>
```